Company Values Graphic

We are looking for a design of our company values that can be used in a variety of places including our website, mousepads, office posters, business cards, etc.

Notes:
- We'd rather have icons/art than photographs on the poster.... so more like an infographic
- The core value group headings are not required, but can be included if you think grouping the values works for your design
- We have a logo for our software product but that logo is not required
- We don't need/want clever images to accompany each value, but some images are fine
- BrisKel logo attached
- BrisKel colors are attached
- BrisKel logo is Nunito Sans ExtraBold 800
- BrisKel website uses Roboto

Our Values - Who we will work with (and who we will not)
The right set of values are essential to building and maintaining a culture that we all wake up eager to be a part of each day. They are foundational to all hiring and firing decisions. They attract the right people and repel the wrong ones.

BE HELPFUL
Make every person and place better because you are there.
Deliver wow with every interaction.

BE HUMBLE
Listen with every muscle.
Passionately help others first.
Seek first to understand.

BE HONEST
Earn trust every day.
Be open and direct.
Treat everyone with fairness and respect.

BE HUMAN
Celebrate passion and action.
Create an environment where people are authentic.
Hire great people and expect a lot from them

BE COURAGEOUS
Dare mighty things.
Make and honor commitments.
All great things start with a small act of courage applied at the right moment.

```html
<!DOCTYPE html>
<html lang="en">
<head>
<meta charset="utf-8">
<title>Our Values</title>
<link href="https://fonts.googleapis.com/css2?family=Roboto:wght@400;700&display=swap" rel="stylesheet">
<style>
  :root {
    --orange: #ff9c00;
    --amber: #ff6400;
    --red: #f70000;
    --ink: #1f1f1f;
    --paper: #ffffff;
    --grass-light: #8fae6a;
    --grass-dark: #5c7f3e;
    --skin: #d9b49a;
  }
  * { margin: 0; padding: 0; box-sizing: border-box; }
  html, body { width: 1200px; height: 1101px; overflow: hidden; background: var(--paper); }
  .canvas {
    position: relative; width: 1200px; height: 1101px; overflow: hidden;
    background: var(--paper);
    font-family: "Roboto", Arial, sans-serif; color: var(--ink);
  }
  .band { position: absolute; height: 46px; }
  .band--top-1 { left: 78px; right: 0; top: 0; background: var(--orange); border-radius: 0 0 0 40px; }
  .band--top-2 { left: 205px; right: 0; top: 42px; background: var(--amber); border-radius: 40px 0 0 40px; }
  .band--top-3 { left: 318px; right: 0; top: 88px; background: var(--red); border-radius: 40px 0 0 40px; }
  .band--bottom-1 { left: 0; width: 905px; top: 965px; background: var(--orange); border-radius: 0 40px 40px 0; }
  .band--bottom-2 { left: 0; width: 1003px; top: 1010px; background: var(--amber); border-radius: 0 40px 40px 0; }
  .band--bottom-3 { left: 0; width: 1102px; top: 1055px; height: 50px; background: var(--red); border-radius: 0 46px 0 0; }

  .photo {
    position: absolute; left: 690px; top: 310px; width: 500px; height: 480px;
    border-radius: 50%;
    background:
      radial-gradient(ellipse at 50% 50%, rgba(217,180,154,0.85) 0%, rgba(217,180,154,0.5) 30%, rgba(143,174,106,0) 55%),
      radial-gradient(ellipse at 50% 50%, var(--grass-dark) 0%, var(--grass-light) 55%, rgba(255,255,255,0) 72%);
  }

  .value { position: absolute; left: 0; width: 1200px; }
  .tag { position: absolute; width: 200px; height: 78px; }
  .tag svg { position: absolute; inset: 0; width: 100%; height: 100%; }
  .tag__label {
    position: absolute; left: 0; top: 16px; width: 188px; text-align: center;
    color: var(--paper); font-weight: 700; font-size: 18px; letter-spacing: 0.2px;
  }
  .copy { position: absolute; left: 293px; font-size: 17.5px; line-height: 23.5px; }
</style>
</head>
<body>
<div class="canvas">
  <div class="band band--top-1"></div>
  <div class="band band--top-2"></div>
  <div class="band band--top-3"></div>

  <div class="photo" role="img" aria-label="Photo of several hands linked together at the wrists in a circle over green grass"></div>

  <section class="value" style="top:0">
    <div class="tag" style="left:66px;top:192px">
      <svg viewBox="0 0 200 78" aria-hidden="true">
        <path d="M6 70 Q70 48 176 50" fill="none" stroke="var(--orange)" stroke-width="5"/>
        <path d="M10 2 H184 Q198 2 194 16 L188 34 Q184 45 170 45 H80 Q30 47 4 64 Q2 30 10 2 Z" fill="var(--red)"/>
      </svg>
      <span class="tag__label">OUR VALUES</span>
    </div>
    <p class="copy" style="left:296px;top:183px">Who we will work with (and who we will not)</p>
    <p class="copy" style="top:214px">The right set of values are essential to building and maintaining a culture that we all wake up<br>eager to be a part of each day. They are foundational to all hiring and firing decisions.<br>They attract the right people and repel the wrong ones.</p>
  </section>

  <section class="value" style="top:0">
    <div class="tag" style="left:66px;top:328px">
      <svg viewBox="0 0 200 78" aria-hidden="true">
        <path d="M6 70 Q70 48 176 50" fill="none" stroke="var(--orange)" stroke-width="5"/>
        <path d="M10 2 H184 Q198 2 194 16 L188 34 Q184 45 170 45 H80 Q30 47 4 64 Q2 30 10 2 Z" fill="var(--red)"/>
      </svg>
      <span class="tag__label">BE HELPFUL</span>
    </div>
    <p class="copy" style="top:324px">Make every person and place better because you are there.<br>Deliver wow with every interaction.</p>
  </section>

  <section class="value" style="top:0">
    <div class="tag" style="left:66px;top:443px">
      <svg viewBox="0 0 200 78" aria-hidden="true">
        <path d="M6 70 Q70 48 176 50" fill="none" stroke="var(--orange)" stroke-width="5"/>
        <path d="M10 2 H184 Q198 2 194 16 L188 34 Q184 45 170 45 H80 Q30 47 4 64 Q2 30 10 2 Z" fill="var(--red)"/>
      </svg>
      <span class="tag__label">BE HUMBLE</span>
    </div>
    <p class="copy" style="top:439px">Listen with every muscle.<br>Passionately help others first.<br>Seek first to understand.</p>
  </section>

  <section class="value" style="top:0">
    <div class="tag" style="left:66px;top:570px">
      <svg viewBox="0 0 200 78" aria-hidden="true">
        <path d="M6 70 Q70 48 176 50" fill="none" stroke="var(--orange)" stroke-width="5"/>
        <path d="M10 2 H184 Q198 2 194 16 L188 34 Q184 45 170 45 H80 Q30 47 4 64 Q2 30 10 2 Z" fill="var(--red)"/>
      </svg>
      <span class="tag__label">BE HONEST</span>
    </div>
    <p class="copy" style="top:567px">Earn trust every day.<br>Be open and direct.<br>Treat everyone with fairness and respect.</p>
  </section>

  <section class="value" style="top:0">
    <div class="tag" style="left:66px;top:696px">
      <svg viewBox="0 0 200 78" aria-hidden="true">
        <path d="M6 70 Q70 48 176 50" fill="none" stroke="var(--orange)" stroke-width="5"/>
        <path d="M10 2 H184 Q198 2 194 16 L188 34 Q184 45 170 45 H80 Q30 47 4 64 Q2 30 10 2 Z" fill="var(--red)"/>
      </svg>
      <span class="tag__label">BE HUMAN</span>
    </div>
    <p class="copy" style="top:690px">Celebrate passion and action.<br>Create an environment where people are authentic.<br>Hire great people and expect a lot from them.</p>
  </section>

  <section class="value" style="top:0">
    <div class="tag" style="left:31px;top:827px;width:240px">
      <svg viewBox="0 0 240 78" preserveAspectRatio="none" aria-hidden="true">
        <path d="M6 70 Q80 48 214 50" fill="none" stroke="var(--orange)" stroke-width="5"/>
        <path d="M10 2 H224 Q238 2 234 16 L228 34 Q224 45 210 45 H90 Q34 47 4 64 Q2 30 10 2 Z" fill="var(--red)"/>
      </svg>
      <span class="tag__label" style="width:228px">BE COURAGEOUS</span>
    </div>
    <p class="copy" style="top:823px">Dare mighty things.<br>Make and honor commitments.<br>All great things start with a small act of courage applied at the right moment.</p>
  </section>

  <div class="band band--bottom-1"></div>
  <div class="band band--bottom-2"></div>
  <div class="band band--bottom-3"></div>
</div>
</body>
</html>
```